Vantor Ridge military/warrior themed clothing company**

eCommerce clothing website

We do have a Shopify account that we would ups like this to be built on for it obvious reasons

We will be starting with the gym/casual wear “Vantor” it will be military style with a unique logo as well as military colours. We will sell this as an exclusive range limited edition to create a scarcity principle which hopefully has our customer desperate to get their gear. We will have it in the colours that Army, Navy and Airforce wear as their undershirts and PT shirts as this will create some great genuine military and KPWR Security origins. Exclusivity is the key.

Having a similar business model and advertising as PulseOtter who have done incredibly well in this area. Our story is better and we just study what sells and how they sell it. Focused on tops namely shirts and singlet and not 1000 choices keep it simple as simple is best and it sells.

Our story

• Veteran Security Company that requires our staff to keep in shape to provide the community with the best service
• No other brands or designers were up to the task of our military styled training, it all thinned, ripped, and looked terrible
• Decided if it’s broken, fix it and do it ourselves
• Trialed and tested every material and design on the market with extensive hours in the gym, outdoor PT, beach sessions, hill runs, boot camps, go till you puke and we did
• Found what worked and put it into action with a limited order just for our staff
• Some of the boys are still servicing and wore the gear to base PT and their fellow serving members wanted to get some of their own gear to which me made limited orders
• Created purpose PT gear with suitable colour scheme to conform with military regs so the boys no longer got in trouble, made limited orders
• Friends and family really liked the gear so after relentless persistence we gave in and made limited orders
• While performing volunteer advocacy work at the KDMs fellow veterans loved the designs and begged for their own gear which would give them confidence and motivation to get back in the gym to rehabilitate and get their health back, it was a no brainer we made limited order
• We began sponsoring local up and coming athletes, fighters and body builders so they could pursue their dream of becoming a professional in their craft again limited orders were made
• Though more relentless desire to obtain our brand and come onboard with our mission statement influencers and celebrities a like urged to endorse and become brand ambassadors so every Australian could feel what it was like to be apart of a genuine grass roots community that had a great story behind it
• And with that Vantor was born
• Stay tuned for the next exciting instalment of what’s to come as we don’t believe in reinventing the wheel but smashing it down completely

A comprehensive range that targets men and women of all ages, fitness levels, body shapes and their specific needs for all times with an exclusive veterans range to support the veteran community.

Top gym brands
Pulse otter
VORN
Tallow brook
Zuma
Omerel
Tavlin

Target Market(s)

men and women 30-45

Industry/Entity Type

Clothing

Number of Pages Required

5+ page

Font styles to use
Sans Serif

Requirements
Must have
• Home page
• white clean back ground
• menu in the top right corner
• search function
• Vantor lettering up the top nice and clean in black
• crisp Vantor shot of the first shoot in both the black and white gold
• headline "forge your legacy" comes across the bottom of the shot above
• men's lifestyle wear section - pre-order now - hyperlink to casual section
• men's active wear section - pre-order now - hyperlink to fitness section
• women's range - coming soon - hyperlink to women's section
• socials and contact (Facebook, Instagram)

Page 2
• our mission
• our story
• our values

Page 3
Change to lifestyle
Follow the format below for order
Functionality to allow pre-order sales for out of stock units

• men's casual wear
- casual singlets
- casual tees
- casual crews
- casual hoodies
- pre-order now

Page 4
Change to active wear

• men's fitness wear
- fitness tees
- fitness crews
- fitness hoodies
- pre-order now

Page 5
• women's section
- coming soon

Australian owed
Australian made
Australian benefit

Throw in an Australian flag

The whole idea was to be bringing in pre-order sales as we wait for the first order to come in from supplier and the next photo shoot we can simply update all the stock pics as needed. For now I have the tec-pac pics that can go in the product pages.

Mission

Building an unstoppable force of warriors that strive for perfection in every aspect of their lives to forge a legacy

Concept

Vantor is an unstoppable force that protect and inspire their own.

Vantor clothing is battle armour to wear as you take the hardest aspects of life to task.

From our struggle comes our resolve.

Tribute

Our fallen warriors and heroes that have come before us, making the ultimate sacrifice, that has allowed our lives to be free and liberated for an unencumbered pursuit of happiness

Story
• Australian family owned and operated
• Veteran led and staffed
• Created to protect those who protect us
• Tried and tested under military conditions
• Australian sourced and produced
• Ethical and environmentally friendly materials
• Restoration of Australian Pride

Values
• Culture
• Community
• Patriotism
• Honour
• Honesty
• Integrity
• Loyalty
• Courage
• Team work
• Success
Nice to have
• To look and feel like one of the big competitors with ease of navigation and ordering
Should not have
• clutter and loading issues

```html
<!DOCTYPE html>
<html lang="en">
<head>
<meta charset="utf-8">
<title>Vantor Ridge — Our Story</title>
<link rel="stylesheet" href="https://fonts.googleapis.com/css2?family=Arimo:wght@400;700&family=Oswald:wght@700&display=swap">
<style>
:root{
  --ink:#000;
  --slate:#414a5a;
  --text:#3c4250;
  --muted:#9aa0aa;
  --panel:#f1f1f5;
  --field:#d6d6d6;
  --footer:#1b1c1f;
  --white:#fff;
}
*{box-sizing:border-box;margin:0;padding:0}
html,body{width:674px;height:1200px;overflow:hidden;background:var(--white)}
body{position:relative;font-family:"Arimo",Arial,sans-serif;color:var(--text)}
.abs{position:absolute}

.site-header{left:0;top:0;width:674px;height:86px;background:var(--white);box-shadow:0 8px 14px rgba(0,0,0,.12);z-index:2}
.brand{left:33px;top:18px;width:176px;font-size:31px;font-weight:700;letter-spacing:2px;color:var(--ink);line-height:1}
.brand-sub{left:33px;top:55px;width:176px;font-size:9px;letter-spacing:3px;color:var(--ink);text-align:center}
.search{left:337px;top:30px;width:177px;height:21px;border-bottom:1px solid #aaa;font-size:9.5px;color:#222;padding-top:3px}
.search svg{position:absolute;right:2px;top:2px}
.account-box{left:540px;top:0;width:62px;height:84px;background:var(--slate)}
.cart-count{left:530px;top:16px;width:19px;height:19px;border:1px solid #000;border-radius:50%;background:#fff;font-size:8px;text-align:center;line-height:17px;color:#000;z-index:3}
.menu{left:627px;top:31px}

.tagline{left:0;top:146px;width:674px;text-align:center;font-size:7.3px;letter-spacing:.8px;color:var(--text)}
.title{left:0;top:180px;width:655px;text-align:center;font-family:"Oswald",Arial,sans-serif;font-size:19px;letter-spacing:1px;color:var(--slate)}
.tribute{left:0;top:212px;width:674px;text-align:center;font-size:8px;line-height:10px;letter-spacing:.4px;color:var(--text)}

.story{font-size:6.6px;line-height:10.8px;letter-spacing:.35px;color:var(--text);text-align:justify}
.story p{margin-bottom:10.8px}
.story b{font-weight:700;font-size:7.2px;letter-spacing:.4px}
.story-col{left:73px;top:284px;width:287px}
.story-wide{left:71px;top:511px;width:531px}
.story-visual{left:373px;top:283px;width:228px;height:218px;background:var(--panel);display:flex;align-items:center;justify-content:center;font-size:30px;font-weight:700;letter-spacing:3px;color:var(--ink)}

.newsletter{left:70px;top:622px;width:534px;height:90px;background:var(--slate);box-shadow:0 10px 18px rgba(0,0,0,.18);text-align:center;color:var(--white)}
.newsletter p{margin-top:21px;font-size:9px;line-height:10.5px;letter-spacing:.4px;padding:0 14px}
.signup{display:flex;justify-content:center;margin-top:10px}
.signup span{display:block;height:19px;font-size:7.4px;line-height:17px;letter-spacing:.4px}
.signup .field{width:164px;background:var(--field);color:#999;border:1px solid #fff}
.signup .btn{width:50px;border:1px solid #fff;border-left:0;color:#fff}

.card{background:var(--panel);text-align:center}
.vision{left:70px;top:770px;width:242px;height:131px}
.values{left:327px;top:769px;width:277px;height:132px}
.card h2{font-weight:400;font-size:19px;letter-spacing:1.2px;color:var(--slate);margin-top:18px}
.values h2{margin-top:21px}
.vision p{font-size:7px;line-height:10px;letter-spacing:.4px;width:170px;margin:18px auto 0}
.value-list{list-style:none;display:grid;grid-template-columns:87px 79px 70px;row-gap:6px;margin:14px 0 0 32px;text-align:left;font-size:7.6px;letter-spacing:.4px}
.value-list li{display:flex;align-items:center;gap:4px;height:10px}

.contact-title{left:0;top:964px;width:662px;text-align:center;font-size:22px;color:var(--slate)}
.contact-sub{left:0;top:1010px;width:662px;text-align:center;font-size:9px;color:var(--text)}
.channel{top:1054px;width:91px;text-align:center}
.channel .dot{width:40px;height:40px;border-radius:50%;background:var(--slate);margin:0 auto;display:flex;align-items:center;justify-content:center}
.channel .label{font-size:7.6px;margin-top:9px;color:var(--text)}
.channel .detail{font-size:6px;margin-top:5px;color:var(--muted)}

.footer-nav{left:0;top:1144px;width:674px;text-align:center;font-size:7.6px;color:var(--text);white-space:nowrap}
.footer-nav i{font-style:normal;margin:0 9px}
.copyright{left:0;top:1174px;width:674px;height:26px;background:var(--footer);color:#8a8d92;font-size:7px;text-align:center;line-height:26px}
</style>
</head>
<body>

<header class="site-header abs">
  <div class="brand abs">VANTOR</div>
  <div class="brand-sub abs">RIDGE</div>
  <div class="search abs">Search our store
    <svg width="24" height="12" viewBox="0 0 24 12"><circle cx="6" cy="6" r="4.5" fill="none" stroke="#222" stroke-width="2"/><circle cx="18" cy="6" r="4.5" fill="none" stroke="#222" stroke-width="2"/><rect x="9" y="3" width="6" height="3" fill="#222"/></svg>
  </div>
  <div class="account-box abs">
    <svg class="abs" style="left:22px;top:14px" width="18" height="22" viewBox="0 0 18 22"><rect x="1" y="6" width="16" height="15" rx="1" fill="none" stroke="#fff" stroke-width="1.4"/><path d="M5 9V5a4 4 0 0 1 8 0v4" fill="none" stroke="#fff" stroke-width="1.4"/></svg>
    <svg class="abs" style="left:22px;top:55px" width="18" height="18" viewBox="0 0 18 18"><circle cx="9" cy="5.5" r="4" fill="none" stroke="#fff" stroke-width="1.6"/><path d="M1.5 17a7.5 7 0 0 1 15 0" fill="none" stroke="#fff" stroke-width="1.6"/></svg>
  </div>
  <div class="cart-count abs">3</div>
  <svg class="menu abs" width="24" height="20" viewBox="0 0 24 20"><rect y="0" width="24" height="3.5" fill="#414a5a"/><rect y="8" width="24" height="3.5" fill="#414a5a"/><rect y="16" width="24" height="3.5" fill="#414a5a"/></svg>
</header>

<p class="tagline abs">AUSTRALIAN OWNED. AUSTRALIAN MADE. ASTURALIAN BENEFIT</p>
<h1 class="title abs">OUR STORY</h1>
<p class="tribute abs">Our fallen warriors and heroes that have come before us, making the ultimate sacrifice,<br>that has allowed our lives to be free and liberated for an unencumbered pursuit of happiness</p>

<section class="story story-col abs">
  <p>It all started when we a “<b>veteran Security Company</b> “required our staff to be in shape to provide the community with the best service. We researched, we looked up at different brand but none of the designers / brands were up to the task of our military<br>Style training. We ended up thinning, ripping and making them look terrible.</p>
  <p>Thats where we went with our Moto <b>“If it’s Broken, Fix it ourself”</b></p>
  <p>We researched materials, tested them with extensive hours in the gym, outdoor PT, Beach session, hill runs, boot camps and basically every thing that will puke us and we did.</p>
  <p><b>Finally</b> we got what we were looking for, we ordered a limited quantity for our staff, some of the boys are still serving and they wore the gear to base PT and before we knew it their fellow members wanted to get a piece of action. We went ahead and make custom PT gear with suitable color scheme to conform with military regs so boys no longer get in trouble again we just make limited order.</p>
  <p>New thing we know friends and family really like the gear so after relentless persistence we gave it and made limited order</p>
</section>
<div class="story-visual abs" role="img" aria-label="Vantor Ridge brand panel">VANTOR</div>

<section class="story story-wide abs">
  <p>While performing volunteer advocacy work at the KDMs fellow veterans loved the designs and begged for their own gear which would give them confidence and motivation to get back in the gym to rehabilitate and get their health back, it was a no brainer we made limited order .</p>
  <p>We began sponsoring local up and coming athletes, fighters and body builders so they could pursue their dream of becoming a professional in their craft again limited orders were made more relentless desire to obtain our brand and come onboard with our mission statement influencers and celebrities a like urged to endorse and become brand ambassadors so every Australian could feel what it was like to be apart of a genuine grass roots community that had a great story behind it. <b>And with it the VANTOR was born</b></p>
</section>

<section class="newsletter abs">
  <p>Stay tuned for the next exciting instalment of what’s to come as we don’t believe in reinventing the wheel but smashing it down completely</p>
  <div class="signup"><span class="field">subscribe to get updates for us</span><span class="btn">Subscribe</span></div>
</section>

<section class="card vision abs">
  <h2>OUR VISION</h2>
  <p>Building an unstoppable force of warriors that strive for perfection in every aspect of their lives to forge a legacy</p>
</section>
<section class="card values abs">
  <h2>OUR VALUES</h2>
  <ul class="value-list">
    <li><svg width="8" height="6" viewBox="0 0 8 6"><path d="M.5 3l2.3 2.3L7.5.5" fill="none" stroke="#777" stroke-width=".8"/></svg>Culture</li>
    <li><svg width="8" height="6" viewBox="0 0 8 6"><path d="M.5 3l2.3 2.3L7.5.5" fill="none" stroke="#777" stroke-width=".8"/></svg>Honesty</li>
    <li><svg width="8" height="6" viewBox="0 0 8 6"><path d="M.5 3l2.3 2.3L7.5.5" fill="none" stroke="#777" stroke-width=".8"/></svg>Team work</li>
    <li><svg width="8" height="6" viewBox="0 0 8 6"><path d="M.5 3l2.3 2.3L7.5.5" fill="none" stroke="#777" stroke-width=".8"/></svg>Community</li>
    <li><svg width="8" height="6" viewBox="0 0 8 6"><path d="M.5 3l2.3 2.3L7.5.5" fill="none" stroke="#777" stroke-width=".8"/></svg>Integrity</li>
    <li><svg width="8" height="6" viewBox="0 0 8 6"><path d="M.5 3l2.3 2.3L7.5.5" fill="none" stroke="#777" stroke-width=".8"/></svg>Success</li>
    <li><svg width="8" height="6" viewBox="0 0 8 6"><path d="M.5 3l2.3 2.3L7.5.5" fill="none" stroke="#777" stroke-width=".8"/></svg>Patriotism</li>
    <li><svg width="8" height="6" viewBox="0 0 8 6"><path d="M.5 3l2.3 2.3L7.5.5" fill="none" stroke="#777" stroke-width=".8"/></svg>Loyalty</li>
    <li></li>
    <li><svg width="8" height="6" viewBox="0 0 8 6"><path d="M.5 3l2.3 2.3L7.5.5" fill="none" stroke="#777" stroke-width=".8"/></svg>Honour</li>
    <li><svg width="8" height="6" viewBox="0 0 8 6"><path d="M.5 3l2.3 2.3L7.5.5" fill="none" stroke="#777" stroke-width=".8"/></svg>Courage</li>
  </ul>
</section>

<h2 class="contact-title abs" style="font-weight:400">Contact us</h2>
<p class="contact-sub abs">We'd love to hear from you</p>

<div class="channel abs" style="left:103px">
  <div class="dot"><svg width="11" height="8" viewBox="0 0 11 8"><rect width="11" height="8" rx="1" fill="#fff"/><path d="M.5 .8l5 3.4 5-3.4" fill="none" stroke="#414a5a" stroke-width="1"/></svg></div>
  <div class="label">Email</div><div class="detail">hello@vantorridge.au</div>
</div>
<div class="channel abs" style="left:194px">
  <div class="dot"><svg width="9" height="9" viewBox="0 0 24 24"><path fill="#fff" d="M6.6 10.8a15.1 15.1 0 0 0 6.6 6.6l2.2-2.2a1 1 0 0 1 1-.25 11.4 11.4 0 0 0 3.6.6 1 1 0 0 1 1 1V20a1 1 0 0 1-1 1A17 17 0 0 1 3 4a1 1 0 0 1 1-1h3.5a1 1 0 0 1 1 1c0 1.25.2 2.45.6 3.6a1 1 0 0 1-.25 1z"/></svg></div>
  <div class="label">Phone</div><div class="detail">555-014-2280</div>
</div>
<div class="channel abs" style="left:285px">
  <div class="dot"><svg width="8" height="11" viewBox="0 0 8 11"><path d="M4 0a4 4 0 0 1 4 4c0 3-4 7-4 7S0 7 0 4a4 4 0 0 1 4-4z" fill="#fff"/><circle cx="4" cy="4" r="1.4" fill="#414a5a"/></svg></div>
  <div class="label">Address</div><div class="detail">18 Ferren Lane, Sydney</div>
</div>
<div class="channel abs" style="left:376px">
  <div class="dot"></div>
  <div class="label">Insta</div><div class="detail">@user_name</div>
</div>
<div class="channel abs" style="left:467px">
  <div class="dot"></div>
  <div class="label">Facebook</div><div class="detail">@user_name</div>
</div>

<nav class="footer-nav abs">Home<i>|</i>Men’s Active Wear<i>|</i>Men’s Life Style Wear<i>|</i>Women’s Range<i>|</i>Terms &amp; Conditions<i>|</i>Returns &amp; Shipping.<i>|.</i>Privacy Policy</nav>
<footer class="copyright abs">Copyright @ 2021, all rights reserved</footer>

</body>
</html>
```